Maple Row Yardcare

I want it as prefession and attractive as possible we are a lawnmowing business

Phone number 605-318-2264
Name- Carl Whitby
Email- mapleroweyardsd@fernpost.net

```html
<!DOCTYPE html>
<html lang="en">
<head>
<meta charset="utf-8">
<title>Maple Row Yardcare – Business Card</title>
<link href="https://fonts.googleapis.com/css2?family=Oswald:wght@500;600&family=Heebo:wght@400;700&display=swap" rel="stylesheet">
<style>
  :root{
    --stage:#1c1c1c;
    --forest:#0a5e3a;
    --forest-deep:#064a2d;
    --leaf:#4cb848;
    --white:#ffffff;
    --paper:#fbfbfb;
  }
  *{box-sizing:border-box;margin:0;padding:0}
  html,body{width:1200px;height:1059px;overflow:hidden;background:var(--stage)}
  .canvas{position:relative;width:1200px;height:1059px}
  .card{position:absolute;left:253px;width:704px;border-radius:22px;overflow:hidden}
  .card--front{top:89px;height:434px;background:var(--paper)}
  .card--back{top:560px;height:416px;background:var(--forest)}

  .brand{position:absolute;left:0;right:0;display:flex;align-items:center;justify-content:center;gap:14px;
    font-family:"Oswald",sans-serif;font-weight:600;text-transform:uppercase;letter-spacing:1px;font-size:58px;line-height:1}
  .brand__dot{width:22px;height:22px;border-radius:50%}
  .card--front .brand{top:96px;color:var(--forest)}
  .card--front .brand__dot{background:var(--forest)}
  .card--back .brand{top:158px;color:var(--white)}
  .card--back .brand__dot{background:var(--white)}

  .services{position:absolute;top:238px;left:0;right:0;text-align:center;font-family:"Oswald",sans-serif;
    font-weight:500;font-size:18px;letter-spacing:2.6px;color:var(--forest-deep)}
  .services .sep{color:var(--leaf);margin:0 6px}

  .contact-band{position:absolute;left:0;right:0;top:283px;bottom:0;background:var(--forest-deep);
    border-top:3px solid var(--leaf)}
  .grass{position:absolute;left:0;right:0;bottom:0;height:95px;
    background:linear-gradient(to bottom,rgba(14,110,60,0),rgba(22,122,64,.55))}
  .holder{position:absolute;top:12px;left:0;right:0;text-align:center;font-family:"Heebo",sans-serif;
    font-weight:700;font-size:31px;color:var(--white)}
  .holder-rule{position:absolute;top:60px;left:221px;width:273px;height:1px;background:var(--leaf)}
  .contacts{position:absolute;top:70px;left:0;right:0;display:flex;justify-content:center;align-items:center;
    font-family:"Heebo",sans-serif;font-size:19px;color:var(--white)}
  .contact{display:flex;align-items:center;gap:12px;height:44px}
  .contact__icon{width:34px;height:34px;border-radius:50%;background:var(--leaf);display:flex;align-items:center;justify-content:center}
  .contacts .divider{width:1px;height:44px;background:var(--leaf);margin:0 20px}
  .contact--mail{font-size:17px}
</style>
</head>
<body>
<div class="canvas">
  <section class="card card--front">
    <div class="brand"><span class="brand__dot"></span><span>Maple Row Yardcare</span></div>
    <p class="services">Lawn Care<span class="sep">•</span>Landscaping<span class="sep">•</span>Yard Maintenance</p>
    <div class="contact-band">
      <div class="grass" role="img" aria-label="Soft silhouette of grass blades along the bottom edge"></div>
      <h1 class="holder">Carl Whitby</h1>
      <div class="holder-rule"></div>
      <div class="contacts">
        <div class="contact contact--phone">
          <span class="contact__icon">
            <svg width="18" height="18" viewBox="0 0 24 24"><path fill="#fff" d="M6.6 10.8a15.1 15.1 0 0 0 6.6 6.6l2.2-2.2c.3-.3.7-.4 1-.2 1.1.4 2.3.6 3.6.6.6 0 1 .4 1 1V20c0 .6-.4 1-1 1A17 17 0 0 1 3 4c0-.6.4-1 1-1h3.5c.6 0 1 .4 1 1 0 1.3.2 2.5.6 3.6.1.3 0 .7-.2 1z"/></svg>
          </span>
          <span>605-318-2264</span>
        </div>
        <span class="divider"></span>
        <div class="contact contact--mail">
          <span class="contact__icon">
            <svg width="18" height="14" viewBox="0 0 24 18"><rect x="1" y="1" width="22" height="16" fill="none" stroke="#fff" stroke-width="2"/><path d="M1 1l11 9 11-9" fill="none" stroke="#fff" stroke-width="2"/></svg>
          </span>
          <span>mapleroweyardsd@fernpost.net</span>
        </div>
      </div>
    </div>
  </section>

  <section class="card card--back">
    <div class="brand"><span class="brand__dot"></span><span>Maple Row Yardcare</span></div>
  </section>
</div>
</body>
</html>
```